Esoteric, wellness company labels

Verdant Quillory is a lifestyle brand with multiple products. We have an offshoot as well called Marrowind Coffee. I need multiple labels or packaging designs that all match so I can start wholesaling.

I want something fun and very eye catching. I have two different logos for Verdant Quillory but just one for the coffee. I’m
Undecided which one I want on the labels because I like both. So either would work. Any coffee products go under marrowind coffee and any other products go under Verdant Quillory.

We sell items such as crystals, tarot and oracle decks, candles, organic coffee, superfood powders and herbs and more.

The items I need labels for should have a streamline look so that all are recognizable as the Verdant Quillory brand. The products that are a priority are:
Organic coffee
Reishi infused coffee
Lion’s Mane infused coffee
Those go under Marrowind Coffee.

Soon I’ll do more items;
Sacred smudging spray
Sacred smudging cleaner
Multiple superfoods
Etc
Updates

We have decided to use compostable coffee bags that are approximately 9x6x33cm so your standard 1lb bag you would see in a store. We still want colorful and eye catching but at the same time being eco friendly. The coffee is 100% organic, free trade, low acid.

We are looking for labels for the coffee but also want to be able to use the same kind of design or similar down the road for our other products. We carry superfood powders (lion’s mane, blue Spirulina, reishi, pearl powder, sea moss etc) but also things like smudging spray, rose water, neroli water, essential oils etc. we are a lifestyle company so we are looking for labels across our store brand items.

Target Market(s)

Esoteric, health and wellness, “new age”

Industry/Entity Type

Retail, wellness,

Colors

Designer to choose colors to be used in the design.

Requirements
Must have
• Beauty, attraction
Should not have
• Anything to do with religion, no dark witchy themes

```html
<!DOCTYPE html>
<html lang="en">
<head>
<meta charset="utf-8">
<title>Marrowind Coffee – Label Options</title>
<link rel="stylesheet" href="https://fonts.googleapis.com/css2?family=Barlow+Condensed:wght@400;500;600&family=Cormorant+Garamond:wght@500&family=Rye&family=Righteous&display=swap">
<style>
  :root {
    --page: #ffffff;
    --stage: #e9f2f8;
    --terracotta: #cf6e4f;
    --terracotta-shadow: #e8c9bb;
    --sage: #5f7f76;
    --ink: #232a45;
    --navy: #1f2a36;
    --amber: #f2a541;
    --rust: #d9733a;
    --cream: #dcdcb8;
    --label-white: #ffffff;
  }
  * { box-sizing: border-box; margin: 0; padding: 0; }
  html, body { width: 848px; height: 1200px; overflow: hidden; background: var(--page); }
  body { position: relative; font-family: "Barlow Condensed", sans-serif; }

  .option { position: absolute; left: 168px; width: 512px; height: 520px; background: var(--stage); }
  .option--one { top: 40px; }
  .option--two { top: 610px; }
  .option-caption { position: absolute; right: 0; top: 528px; font-size: 15px; font-weight: 600; color: #111; }

  /* Option 1: white label */
  .label-light {
    position: absolute; left: 106px; top: 30px; width: 300px; height: 460px;
    background: var(--label-white); display: flex; flex-direction: column; align-items: center;
    box-shadow: 0 1px 4px rgba(30,40,60,.12);
  }
  .arched-title { margin-top: 22px; width: 220px; height: 70px; }
  .arched-title text { font-family: "Rye", serif; font-size: 40px; fill: var(--terracotta); letter-spacing: 1px; }
  .arched-title .title-shadow { fill: var(--terracotta-shadow); }
  .botanical-arch {
    width: 130px; height: 190px; margin-top: 2px;
    border: 1.5px solid var(--sage); border-radius: 65px 65px 4px 4px;
    background: linear-gradient(180deg, #fbefe9 0%, #eef3f0 100%);
  }
  .tagline-caps { margin-top: 16px; font-size: 19px; font-weight: 500; color: var(--terracotta); letter-spacing: .3px; }
  .brand-name {
    margin-top: 14px; font-family: "Cormorant Garamond", serif; font-weight: 500;
    font-size: 13px; letter-spacing: 4px; color: var(--ink); text-align: center; line-height: 1.25;
  }
  .weight-light { margin-top: 16px; font-size: 14px; color: var(--terracotta); }
  .spark { margin-top: 14px; }

  /* Option 2: dark label */
  .label-dark {
    position: absolute; left: 121px; top: 50px; width: 270px; height: 420px;
    background: var(--navy); border: 5px solid var(--rust); border-radius: 16px;
    display: flex; flex-direction: column; align-items: center;
  }
  .bird-arch {
    margin-top: 58px; width: 120px; height: 132px; border-radius: 60px 60px 0 0;
    background: linear-gradient(160deg, var(--cream) 0%, #e9b27a 55%, var(--rust) 100%);
  }
  .display-title { margin-top: 16px; font-family: "Righteous", sans-serif; font-size: 56px; line-height: 1; color: var(--amber); letter-spacing: 1px; }
  .tagline-soft { margin-top: 2px; font-size: 18px; color: var(--cream); }
  .weight-dark { margin-top: 60px; font-size: 12px; color: var(--cream); }
</style>
</head>
<body>
  <section class="option option--one">
    <article class="label-light">
      <svg class="arched-title" viewBox="0 0 220 70" aria-label="Coffee">
        <defs><path id="arc" d="M20 66 Q110 -4 200 66"/></defs>
        <text class="title-shadow" dx="2" dy="2"><textPath href="#arc" startOffset="50%" text-anchor="middle">COFFEE</textPath></text>
        <text><textPath href="#arc" startOffset="50%" text-anchor="middle">COFFEE</textPath></text>
      </svg>
      <div class="botanical-arch" role="img" aria-label="Line illustration of a coffee plant sprig beneath a falling star inside an arch"></div>
      <p class="tagline-caps">ROASTED IN CALIFORNIA</p>
      <p class="brand-name">VERDANT<br>QUILLORY</p>
      <p class="weight-light">250 g &nbsp;•&nbsp; 8.8 oz</p>
      <svg class="spark" width="18" height="18" viewBox="0 0 18 18" aria-hidden="true">
        <path d="M9 0V18M0 9H18M3 3L15 15M15 3L3 15" stroke="var(--sage)" stroke-width="1"/>
      </svg>
    </article>
    <p class="option-caption">Option 1</p>
  </section>

  <section class="option option--two">
    <article class="label-dark">
      <div class="bird-arch" role="img" aria-label="Illustration of a songbird perched on a leafy orange branch inside an arch"></div>
      <h2 class="display-title">COFFEE</h2>
      <p class="tagline-soft">Roasted in California</p>
      <p class="weight-dark">250 g &nbsp;•&nbsp; 8.8 oz</p>
    </article>
    <p class="option-caption">Option 2</p>
  </section>
</body>
</html>
```